A5 Flyers - 4 per page front and back - GlenmoorTrade

Design an A5 flyer (148 x 105mm) in Landscape mode. Allow 4 flyers to be printed per A4 sheet. Company logo and colours provided, along with the words. Designer required to provide a simple but striking design using the company colours, the rest is up to the designer. See further details in the attachments.

```html
<!DOCTYPE html>
<html lang="en">
<head>
<meta charset="utf-8">
<title>GlenmoorTrade – Flyers 1</title>
<link rel="stylesheet" href="https://fonts.googleapis.com/css2?family=Ubuntu:wght@500;700&family=Open+Sans:wght@400;600&display=swap">
<style>
  :root {
    --orange: #e2621b;
    --orange-text: #f07a1c;
    --slate: #4a4e59;
    --body-grey: #555a62;
    --footer-grey: #e0e0e0;
    --frame: #8a8a8a;
    --paper: #ffffff;
  }
  * { margin: 0; padding: 0; box-sizing: border-box; }
  html, body { width: 1200px; height: 1200px; overflow: hidden; background: var(--paper); }
  .sheet { position: relative; width: 1200px; height: 1200px; overflow: hidden; font-family: "Open Sans", Arial, sans-serif; }

  .sheet-title {
    position: absolute; top: 68px; left: 0; width: 1200px; text-align: center;
    font-family: "Ubuntu", sans-serif; font-weight: 700; font-size: 27px; color: var(--slate);
  }

  .flyer {
    position: absolute; width: 583px; height: 413px; overflow: hidden;
    border: 1px solid var(--frame); background: var(--paper);
  }
  .flyer .shapes { position: absolute; inset: 0; width: 100%; height: 100%; }

  .cover .brand-name {
    position: absolute; top: 105px; left: 0; width: 583px; text-align: center;
    font-family: "Ubuntu", sans-serif; font-weight: 700; font-size: 50px; color: var(--orange);
    letter-spacing: 1px;
  }
  .cover .headline {
    position: absolute; top: 217px; left: 0; width: 583px; text-align: center;
    font-family: "Ubuntu", sans-serif; font-weight: 500; font-size: 27px; color: var(--orange);
  }
  .cover .subtitle {
    position: absolute; top: 287px; left: 0; width: 583px; text-align: center;
    font-family: "Ubuntu", sans-serif; font-weight: 500; font-size: 27px; color: var(--slate);
  }

  .story .headline {
    position: absolute; top: 62px; left: 0; width: 583px; text-align: center;
    font-family: "Ubuntu", sans-serif; font-weight: 500; font-size: 26px; color: var(--orange);
  }
  .story .body {
    position: absolute; left: 0; width: 583px; text-align: center;
    font-size: 12.6px; line-height: 18px; color: var(--body-grey);
  }
  .story .body.first { top: 112px; }
  .story .body.second { top: 220px; }
  .story .highlight { color: var(--orange-text); font-weight: 600; }

  .footer {
    position: absolute; left: 0; bottom: 0; width: 583px; height: 39px;
    font-size: 11px; color: #4a4a4a;
  }
  .footer .web { position: absolute; left: 29px; top: 13px; }
  .footer .social { position: absolute; left: 205px; top: 13px; display: flex; align-items: center; gap: 6px; }
  .footer .social .dot { width: 11px; height: 11px; border: 1px solid #6a6a6a; border-radius: 50%; }
  .footer .brand-mini {
    position: absolute; right: 12px; top: 11px;
    font-family: "Ubuntu", sans-serif; font-weight: 700; font-size: 14px; color: var(--orange);
  }

  .label {
    position: absolute; font-family: "Ubuntu", sans-serif; font-weight: 700; font-size: 26px;
    color: var(--slate); width: 40px; text-align: center;
  }
</style>
</head>
<body>
<main class="sheet">
  <h1 class="sheet-title">Flyers 1</h1>

  <!-- Row 1 -->
  <section class="flyer cover" style="left:18px; top:137px;">
    <svg class="shapes" viewBox="0 0 728 515" preserveAspectRatio="none" aria-hidden="true">
      <polygon points="0,0 150,0 58,284 0,159" fill="var(--slate)"/>
      <polygon points="0,159 165,515 0,515" fill="var(--orange)"/>
    </svg>
    <div class="brand-name">GlenmoorTrade</div>
    <h2 class="headline">We can reach the world - quickly</h2>
    <p class="subtitle">A briefcase study</p>
  </section>

  <section class="flyer story" style="left:600px; top:137px;">
    <svg class="shapes" viewBox="0 0 728 515" preserveAspectRatio="none" aria-hidden="true">
      <polygon points="0,0 475,0 300,25 0,65" fill="var(--orange)"/>
      <polygon points="475,0 728,0 728,60 300,25" fill="var(--slate)"/>
      <polygon points="0,441 245,466 0,466" fill="var(--slate)"/>
      <polygon points="728,434 728,466 540,466" fill="var(--orange)"/>
    </svg>
    <h2 class="headline">We can reach the world - quickly</h2>
    <p class="body first">A <span class="highlight">GlenmoorTrade</span> member recently posted a request for an urgent Oil Cooler.<br>
      The <span class="highlight">GlenmoorTrade</span> unique broadcast system using email and social media<br>
      streams made contact with over 100,000 users all over the world in minutes -<br>
      quicker than a purchasing officer can search for one or two alternate suppliers.</p>
    <p class="body second">Remember, its not just your industry that uses that particular spare part, many<br>
      industries share the same parts, and in many cases the part you require is a lot<br>
      closer to you than you think…..you just don’t know who to contact.<br>
      The <span class="highlight">GlenmoorTrade</span> broadcast is anonymous and quick.</p>
    <footer class="footer" style="background:var(--footer-grey);">
      <span class="web">www.glenmoortrade.com</span>
      <span class="social"><span class="dot"></span>@glenmoortrade</span>
      <span class="brand-mini">GlenmoorTrade</span>
    </footer>
  </section>

  <span class="label" style="left:289px; top:565px;">A</span>
  <span class="label" style="left:872px; top:565px;">B</span>

  <!-- Row 2 -->
  <section class="flyer cover" style="left:18px; top:650px;">
    <svg class="shapes" viewBox="0 0 728 515" preserveAspectRatio="none" aria-hidden="true">
      <polygon points="0,0 150,0 58,284 0,159" fill="var(--slate)"/>
      <polygon points="0,159 165,515 0,515" fill="var(--orange)"/>
    </svg>
    <div class="brand-name">GlenmoorTrade</div>
    <h2 class="headline">We keep your issue quiet</h2>
    <p class="subtitle">A briefcase study</p>
  </section>

  <section class="flyer story" style="left:600px; top:650px;">
    <svg class="shapes" viewBox="0 0 728 515" preserveAspectRatio="none" aria-hidden="true">
      <polygon points="0,0 475,0 300,25 0,65" fill="var(--orange)"/>
      <polygon points="475,0 728,0 728,60 300,25" fill="var(--slate)"/>
      <polygon points="0,441 245,466 0,466" fill="var(--slate)"/>
      <polygon points="728,434 728,466 540,466" fill="var(--orange)"/>
    </svg>
    <h2 class="headline">We keep your issue quiet</h2>
    <p class="body first">A major mining company had a failure of a conveyor belt. The company had<br>
      sourced a replacement belt, but this was weeks from being delivered, and the<br>
      mining company could not afford extended downtime.</p>
    <p class="body second">Anonymously <span class="highlight">GlenmoorTrade</span> advertised the requirement, and alternate sources<br>
      of supply were quickly identified without the mining company needing to reveal<br>
      their equipment failure. The mining company could then determine who they<br>
      wanted to deal with and complete the transaction under their control.</p>
    <footer class="footer" style="background:var(--footer-grey);">
      <span class="web">www.glenmoortrade.com</span>
      <span class="social"><span class="dot"></span>@glenmoortrade</span>
      <span class="brand-mini">GlenmoorTrade</span>
    </footer>
  </section>

  <span class="label" style="left:289px; top:1092px;">A</span>
  <span class="label" style="left:872px; top:1092px;">B</span>
</main>
</body>
</html>
```